Women's health flyer for Vindmark Health & Wellness . for a Women's health conference

I need a flyer , post card 4x 6 or 5 x 7 sized designed , 2 sides focused on my business branding and Women's health. we deliver bespoke care and focus on all phases of women's health and life. I want something aligned with our bespoke whole person care philosophy and that is fresh and forward thinking.
www.vindmark-care.com
This is to help women know they can have care for all phases of life , fertility , postpartum , perimenopause , mental health , wellness, weight loss, increased energy stress , menopause etc
please use knowledge from website about my company , www.vindmark-care.com
I also feel like my brand kit could use an additional secondarily color option in it

Target Market(s)

Women 25-70

Industry/Entity Type

health & Wellness

Colors
0054AA
0677BA
7BADD7
CADEEF
E8F1F8
0094D4
00A9DD
6FCCEA
C7EBF8
E9F6FB
00AB8E
00BBA5
67D7C9
C6EFE9
E9F9F6
59FF00
82FF00
B8FF75
E3FFCB
F4FFEA
E54698
E96AAD
F1A4CE
F9D9EA
FCEFF6
A7469A
B969AE
D3A5CF
EDDBEB
F8F0F9

Requirements
Must have
• photos , my logo, connection to my brand
Nice to have
• something fresh and different
Should not have
• look like a genetic "wellness program"

```html
<!DOCTYPE html>
<html lang="en">
<head>
<meta charset="utf-8">
<title>Vindmark Health &amp; Wellness – Postcard</title>
<link rel="stylesheet" href="https://fonts.googleapis.com/css2?family=Poppins:wght@400;500;600;700&display=swap">
<style>
  :root{
    --navy:#0b5c96;
    --blue:#0677ba;
    --cyan:#00a9dd;
    --sky:#6fccea;
    --green:#62b146;
    --green-dark:#4e9a35;
    --ink:#1d1d1d;
    --white:#ffffff;
    --stage:#e6e7e8;
    --stamp:#d2d3d4;
  }
  *{margin:0;padding:0;box-sizing:border-box}
  html,body{width:1067px;height:1200px;overflow:hidden}
  body{background:var(--stage);font-family:'Poppins',sans-serif;color:var(--ink);position:relative}
  .card{position:absolute;left:133px;width:800px;height:571px;background:var(--white);overflow:hidden;box-shadow:0 2px 8px rgba(0,0,0,.12)}
  .card--front{top:19px}
  .card--back{top:610px}
  .card__art{position:absolute;inset:0;width:800px;height:571px}
  .abs{position:absolute}

  /* brand lockup */
  .brand{position:absolute;display:flex;flex-direction:column;align-items:center;color:var(--navy);font-weight:600;text-align:center;line-height:1.1;white-space:nowrap}
  .brand__dot{width:30px;height:30px;border-radius:50%;background:var(--cyan);margin-bottom:12px}
  .brand__name{font-size:44px;letter-spacing:1px}
  .brand__sub{font-size:12.5px;letter-spacing:5px;margin-top:6px}
  .card--front .brand{left:40px;top:30px;width:300px}
  .card--back .brand{left:430px;top:28px;width:190px}
  .card--back .brand__dot{width:22px;height:22px;margin-bottom:8px}
  .card--back .brand__name{font-size:25px;letter-spacing:.5px}
  .card--back .brand__sub{font-size:7px;letter-spacing:2.6px;margin-top:4px}

  /* front */
  .headline{left:50px;top:226px;color:var(--white);font-weight:700;font-size:23px;line-height:28px;white-space:nowrap}
  .concerns{left:50px;top:323px;color:var(--white);font-size:12.3px;line-height:15.5px;white-space:nowrap}
  .about{left:50px;top:406px;font-size:12px;font-weight:500;line-height:15.5px;white-space:nowrap}
  .front-contact{left:64px;top:520px;display:flex;align-items:center;gap:14px;color:var(--white);font-weight:600;font-size:18.5px}
  .front-contact__item{display:flex;align-items:center;gap:7px}
  .front-contact__rule{width:2px;height:20px;background:var(--white)}
  .icon-chip{width:20px;height:20px;border-radius:50%;background:var(--white);display:flex;align-items:center;justify-content:center}

  /* back */
  .services-title{left:48px;top:34px;width:284px;height:26px;border-radius:13px;background:var(--green);color:var(--white);font-weight:700;font-size:19px;line-height:26px;text-align:center}
  .services-intro{left:76px;top:66px;font-size:12.5px}
  .service-list{left:52px;top:93px;list-style:none}
  .service{display:flex;align-items:center;gap:14px;height:37px;font-weight:600;font-size:12.3px;line-height:14px}
  .service__icon{width:34px;height:34px;border-radius:50%;background:var(--navy);border:3px solid var(--white);box-shadow:0 0 0 2px var(--green);display:flex;align-items:center;justify-content:center;flex:none}
  .contact-title{left:48px;top:423px;color:var(--white);font-weight:700;font-size:21px}
  .contact-list{left:48px;top:458px;list-style:none;color:var(--white);font-weight:600;font-size:16px}
  .contact-list li{display:flex;align-items:center;gap:10px;height:27px}
  .contact-dot{width:17px;height:17px;border-radius:50%;background:var(--green);flex:none;display:flex;align-items:center;justify-content:center}
  .stamp-box{left:681px;top:28px;width:88px;height:86px;background:var(--stamp)}
</style>
</head>
<body>

<!-- FRONT -->
<section class="card card--front">
  <svg class="card__art" viewBox="0 0 800 571">
    <defs>
      <linearGradient id="beachGlow" x1="0" y1="0" x2="1" y2="1">
        <stop offset="0" stop-color="#f4efe6"/>
        <stop offset=".35" stop-color="#f7d58a"/>
        <stop offset=".7" stop-color="#e9c9a2"/>
        <stop offset="1" stop-color="#c9a27a"/>
      </linearGradient>
      <linearGradient id="seaRocks" x1="0" y1="0" x2="0" y2="1">
        <stop offset="0" stop-color="#b9d7e2"/>
        <stop offset=".45" stop-color="#5f9fb0"/>
        <stop offset=".7" stop-color="#8a6b4c"/>
        <stop offset="1" stop-color="#5b4633"/>
      </linearGradient>
      <linearGradient id="arcBlue" x1="0" y1="0" x2="1" y2="1">
        <stop offset="0" stop-color="#00a9dd"/>
        <stop offset="1" stop-color="#0054aa"/>
      </linearGradient>
    </defs>
    <g role="img" aria-label="Photo: woman in a sun hat raising her arms on a sunlit beach">
      <path d="M388 0 L800 0 L800 430 C660 402 530 345 478 245 C438 165 398 85 388 0 Z" fill="url(#beachGlow)"/>
    </g>
    <path d="M334 0 L388 0 C398 85 438 165 478 245 C530 345 660 402 800 430 L800 470 C630 445 490 365 428 245 C388 165 344 85 334 0 Z" fill="url(#arcBlue)"/>
    <path d="M0 212 L408 212 C428 262 458 300 500 332 L548 388 L0 388 Z" fill="var(--green)"/>
    <circle cx="526" cy="287" r="101" fill="var(--blue)"/>
    <circle cx="526" cy="287" r="93" fill="var(--white)"/>
    <g role="img" aria-label="Photo: rocky jetty stretching into a calm sea">
      <circle cx="526" cy="287" r="87" fill="url(#seaRocks)"/>
    </g>
    <path d="M0 498 C260 462 540 462 800 508 L800 524 C540 478 260 478 0 514 Z" fill="var(--cyan)"/>
    <path d="M0 514 C260 478 540 478 800 524 L800 571 L0 571 Z" fill="var(--navy)"/>
  </svg>

  <div class="brand">
    <span class="brand__dot"></span>
    <span class="brand__name">VINDMARK</span>
    <span class="brand__sub">HEALTH &amp; WELLNESS</span>
  </div>

  <h1 class="abs headline">We deliver bespoke care<br>and focus on all phases<br>of women's health and life.</h1>
  <p class="abs concerns">care for all phases of life • fertility • postpartum •<br>perimenopause • mental health • wellness •<br>weight loss • increased energy stress • menopause</p>
  <p class="abs about">Vindmark combines Traditional Eastern Medicine (T.E.A.M) with modern practices, offering<br>a holistic approach to well-being. This approach considers the interconnectedness of<br>mind, body, and spirit, truly taking the whole person approach to wellbeing</p>

  <div class="abs front-contact">
    <span class="front-contact__item">
      <span class="icon-chip"><svg width="12" height="12" viewBox="0 0 24 24"><path fill="#0b5c96" d="M6.6 10.8a15 15 0 0 0 6.6 6.6l2.2-2.2a1 1 0 0 1 1-.25 11.4 11.4 0 0 0 3.6.57 1 1 0 0 1 1 1V20a1 1 0 0 1-1 1A17 17 0 0 1 3 4a1 1 0 0 1 1-1h3.5a1 1 0 0 1 1 1c0 1.25.2 2.45.57 3.57a1 1 0 0 1-.25 1z"/></svg></span>
      +1-816-555-0147
    </span>
    <span class="front-contact__rule"></span>
    <span class="front-contact__item">
      <span class="icon-chip"><svg width="13" height="13" viewBox="0 0 24 24" fill="none" stroke="#0b5c96" stroke-width="2.2"><circle cx="12" cy="12" r="9"/><path d="M3 12h18M12 3c3 3.5 3 14.5 0 18M12 3c-3 3.5-3 14.5 0 18"/></svg></span>
      www.vindmark-care.com
    </span>
  </div>
</section>

<!-- BACK -->
<section class="card card--back">
  <svg class="card__art" viewBox="0 0 800 571">
    <defs>
      <linearGradient id="lakeScene" x1="0" y1="0" x2="0" y2="1">
        <stop offset="0" stop-color="#cfe3f2"/>
        <stop offset=".35" stop-color="#8fb8d9"/>
        <stop offset=".5" stop-color="#3f6b3a"/>
        <stop offset=".75" stop-color="#8fb2c9"/>
        <stop offset="1" stop-color="#5d7d4a"/>
      </linearGradient>
      <linearGradient id="arcBlueBack" x1="1" y1="0" x2="0" y2="1">
        <stop offset="0" stop-color="#00a9dd"/>
        <stop offset="1" stop-color="#0054aa"/>
      </linearGradient>
    </defs>
    <g role="img" aria-label="Photo: boardwalk beside a forest lake under a cloudy sky">
      <path d="M0 300 C300 298 418 200 400 110 L400 430 L0 430 Z" fill="url(#lakeScene)"/>
    </g>
    <path d="M390 0 L418 0 C430 200 300 306 0 315 L0 292 C290 285 408 190 390 0 Z" fill="url(#arcBlueBack)"/>
    <path d="M0 380 C170 368 340 410 432 571 L412 571 C322 425 160 392 0 398 Z" fill="var(--cyan)"/>
    <path d="M0 398 C160 392 322 425 412 571 L0 571 Z" fill="var(--navy)"/>
  </svg>

  <h2 class="abs services-title">Our Services</h2>
  <p class="abs services-intro">Join us in this revolution of wellbeing</p>
  <ul class="abs service-list">
    <li class="service"><span class="service__icon"><svg width="14" height="14" viewBox="0 0 24 24"><path fill="#fff" d="M12 3c3 4 3 9 0 15c-3-6-3-11 0-15zM3 10c5 0 8 3 9 8c-5 0-8-3-9-8zM21 10c0 5-4 8-9 8c1-5 4-8 9-8z"/></svg></span>Customized Corporate Wellness</li>
    <li class="service"><span class="service__icon"><svg width="14" height="14" viewBox="0 0 24 24"><path fill="#fff" d="M5 14h14l-2 6H7zM11 3h2v10h-2z"/></svg></span>Acupunture &amp; Traditional<br>East Asian Medicine</li>
    <li class="service"><span class="service__icon"><svg width="14" height="14" viewBox="0 0 24 24"><circle cx="12" cy="6" r="3" fill="#fff"/><path fill="#fff" d="M4 20c2-6 5-9 8-9s6 3 8 9z"/></svg></span>Retreats</li>
    <li class="service"><span class="service__icon"><svg width="14" height="14" viewBox="0 0 24 24"><circle cx="12" cy="8" r="3.5" fill="#fff"/><path fill="#fff" d="M6 20c0-4 3-7 6-7s6 3 6 7z"/></svg></span>Individual Coaching</li>
    <li class="service"><span class="service__icon"><svg width="14" height="14" viewBox="0 0 24 24"><rect x="4" y="4" width="16" height="11" rx="1" fill="#fff"/><path fill="#fff" d="M11 15h2v5h-2zM7 20h10v1.5H7z"/></svg></span>Workshops</li>
  </ul>

  <h2 class="abs contact-title">Contact</h2>
  <ul class="abs contact-list">
    <li><span class="contact-dot"><svg width="9" height="9" viewBox="0 0 24 24"><path fill="#fff" d="M6.6 10.8a15 15 0 0 0 6.6 6.6l2.2-2.2a1 1 0 0 1 1-.25 11.4 11.4 0 0 0 3.6.57 1 1 0 0 1 1 1V20a1 1 0 0 1-1 1A17 17 0 0 1 3 4a1 1 0 0 1 1-1h3.5a1 1 0 0 1 1 1c0 1.25.2 2.45.57 3.57a1 1 0 0 1-.25 1z"/></svg></span>+1-816-555-0147</li>
    <li><span class="contact-dot"><svg width="9" height="9" viewBox="0 0 24 24" fill="none" stroke="#fff" stroke-width="2.5"><rect x="3" y="6" width="18" height="12"/><path d="M3 6l9 7 9-7"/></svg></span>nora@norawestfield.com</li>
    <li><span class="contact-dot"><svg width="9" height="9" viewBox="0 0 24 24" fill="none" stroke="#fff" stroke-width="2.5"><circle cx="12" cy="12" r="9"/><path d="M3 12h18M12 3v18"/></svg></span>www.vindmark-care.com</li>
  </ul>

  <div class="brand">
    <span class="brand__dot"></span>
    <span class="brand__name">VINDMARK</span>
    <span class="brand__sub">HEALTH &amp; WELLNESS</span>
  </div>
  <div class="abs stamp-box"></div>
</section>

</body>
</html>
```